Harbor Business Cards

I need a business card designed with the following information.

Company Name: Harbor Wealth Management
Name: BriAnne Dockery
Title: Executive Assistant
Cell: (555) 555-0173
Direct Line: (555) 555-0148
Email: brianne@harborwmx.com
Address: 20537 W. Marlowe PKWY Ste. B
Larkfield, TX 77390

I have attached the logo.
I would like it in navy blue and silver.
Thanks.

```html
<!DOCTYPE html>
<html lang="en">
<head>
<meta charset="utf-8">
<title>Harbor Wealth Management – Business Card</title>
<link rel="stylesheet" href="https://fonts.googleapis.com/css2?family=Marcellus&family=Mulish:wght@400;700&display=swap">
<style>
  :root {
    --navy: #0b1746;
    --silver: #e6edf1;
    --page: #d4d9de;
    --edge: #1a1f2b;
    --white: #ffffff;
  }
  * { margin: 0; padding: 0; box-sizing: border-box; }
  html, body { width: 1200px; height: 1200px; overflow: hidden; }
  body { background: var(--page); position: relative; font-family: "Mulish", sans-serif; color: var(--navy); }

  .card {
    position: absolute;
    left: 140px;
    width: 920px;
    height: 540px;
    background: var(--silver);
    border: 1.5px solid var(--edge);
    border-radius: 44px 44px 44px 0;
    overflow: hidden;
  }
  .card--front { top: 40px; }
  .card--back { top: 620px; }

  .wordmark { position: absolute; font-family: "Marcellus", serif; font-weight: 400; color: var(--navy); white-space: nowrap; text-align: center; }
  .wordmark__name { display: block; }
  .wordmark__sub { display: block; }

  .card--front .wordmark { left: 0; right: 0; top: 200px; }
  .card--front .wordmark__name { font-size: 70px; line-height: 1; letter-spacing: 0.55em; padding-left: 0.55em; }
  .card--front .wordmark__sub { margin-top: 30px; font-size: 28px; letter-spacing: 0.32em; padding-left: 0.32em; }

  .card--back .wordmark { right: 60px; top: 50px; width: 405px; }
  .card--back .wordmark__name { font-size: 50px; line-height: 1; letter-spacing: 0.5em; padding-left: 0.5em; }
  .card--back .wordmark__sub { margin-top: 16px; font-size: 19px; letter-spacing: 0.3em; padding-left: 0.3em; }

  .icon-band { position: absolute; left: 0; top: 0; width: 200px; height: 540px; }

  .contact { position: absolute; left: 181px; top: 252px; }
  .contact__name { font-weight: 700; font-size: 23px; line-height: 28px; }
  .contact__title { font-size: 19px; line-height: 26px; margin-bottom: 20px; }
  .contact__line { font-size: 19px; line-height: 31.5px; white-space: nowrap; }
</style>
</head>
<body>

<section class="card card--front">
  <div class="wordmark">
    <span class="wordmark__name">HARBOR</span>
    <span class="wordmark__sub">WEALTH MANAGEMENT</span>
  </div>
</section>

<section class="card card--back">
  <svg class="icon-band" viewBox="0 0 200 540" aria-hidden="true">
    <rect fill="var(--navy)" x="0" y="310" width="163" height="160"/>
    <g fill="none" stroke="var(--white)" stroke-width="1.4" stroke-linecap="round" stroke-linejoin="round">
      <rect x="138" y="334" width="9" height="15" rx="1.5"/>
      <line x1="141.5" y1="346" x2="143.5" y2="346"/>
      <path d="M137 365 q2 7 10 10" stroke-width="2.4"/>
      <rect x="136" y="397" width="14" height="10"/>
      <path d="M136 397 l7 6 l7 -6 M136 407 l5 -5 M150 407 l-5 -5"/>
      <path d="M143 437 a4.5 4.5 0 1 0 0.01 0 Z M143 446 l0 3"/>
      <path d="M137 448 q6 4 12 0"/>
    </g>
  </svg>

  <div class="wordmark">
    <span class="wordmark__name">HARBOR</span>
    <span class="wordmark__sub">WEALTH MANAGEMENT</span>
  </div>

  <div class="contact">
    <p class="contact__name">BriAnne Dockery</p>
    <p class="contact__title">Executive Assistant</p>
    <p class="contact__line">(555) 555-0173</p>
    <p class="contact__line">(555) 555-0148</p>
    <p class="contact__line">brianne@harborwmx.com</p>
    <p class="contact__line">20537 W. Marlowe PKWY Ste. B Larkfield, TX 77390</p>
  </div>
</section>

</body>
</html>
```